Flyer or Info graphic required -for journey map/flow chart

I would like a info graphic designed around the Australian home buying process. explaining all the steps along the way and how it a fits together from the start all the way to settlement and when you pick up the keys.

i want it to be clear and simple. there is quite a lot of words and so the design needs to be simple so they can take it all in.
I have attached an example of one i have seen to give you an idea of what i am thinking as well as the required words

Target Market(s)

25-35 year old first time home buyers

Industry/Entity Type

Financial Service

Font styles to use
Sans Serif

Colors
0355a3

Requirements
Must have
• the word document attached called "start" has the steps i want in my document.
• there is also a hand drawn picture (untitled document) with a portion in yellow, this reflects a certain stage of the process called "cooling off" and it needs to be highlighted as one stage.
• there are also days mentioned on this document so readers understand how long things take
Nice to have
• Logo and Web Address & corporate colours

```html
<!DOCTYPE html>
<html lang="en">
<head>
<meta charset="utf-8">
<title>First Key Loans – Steps in Buying Your First Home</title>
<link rel="stylesheet" href="https://fonts.googleapis.com/css2?family=Montserrat:wght@400;500;600;700;800&display=swap">
<style>
  :root {
    --bg: #3a3b40;
    --white: #ffffff;
    --blue-accent: #2a9de6;
    --blue-num: #2b93dc;
    --blue-brand: #1f8fe0;
    --cell-dark: #1f80c8;
    --cell-mid: #2a8cd3;
    --cell-light: #46b6e9;
    --cell-teal: #3fbfc6;
    --cell-ink: #1c3556;
    --start-red: #d6384a;
  }
  * { box-sizing: border-box; margin: 0; padding: 0; }
  html, body { width: 1200px; height: 784px; overflow: hidden; background: var(--bg); }
  body { font-family: "Montserrat", Arial, sans-serif; color: var(--white); }

  .poster { position: relative; width: 1200px; height: 784px; overflow: hidden; background: var(--bg); }

  .brand {
    position: absolute; top: 44px; left: 0; width: 1200px; text-align: center;
    font-size: 34px; font-weight: 800; color: var(--blue-brand); letter-spacing: -0.5px;
  }

  .headline {
    position: absolute; top: 127px; left: 0; width: 1200px; text-align: center;
    font-size: 15px; font-weight: 500; line-height: 1.45;
  }

  .journey { position: absolute; left: 0; top: 0; }
  .journey .cell-num { font-family: "Montserrat", Arial, sans-serif; font-size: 28px; font-weight: 700; fill: var(--cell-ink); text-anchor: middle; dominant-baseline: central; }
  .journey .start-label { font-family: "Montserrat", Arial, sans-serif; font-size: 25px; font-weight: 700; fill: var(--white); text-anchor: middle; dominant-baseline: central; }
  .journey .marker { font-family: "Montserrat", Arial, sans-serif; font-size: 10.5px; font-weight: 700; fill: var(--blue-accent); }
  .journey .marker-line { stroke: var(--blue-accent); stroke-width: 1.3; }
  .journey .marker-dot { fill: var(--blue-accent); }

  .step { position: absolute; display: flex; font-size: 7.6px; line-height: 1.3; font-weight: 500; }
  .step-num { color: var(--blue-num); font-size: 22px; font-weight: 700; line-height: 0.9; width: 22px; flex: none; text-align: right; margin-right: 6px; }
  .step-body { padding-top: 2px; }
  .step-body p { margin: 0; }
  .step-body .sub { color: var(--blue-accent); font-weight: 600; }
  .col-left .step { left: 24px; width: 230px; }
  .col-right .step { left: 918px; width: 250px; }
</style>
</head>
<body>
<div class="poster">

  <div class="brand">First Key Loans</div>

  <h1 class="headline">Overview to understand all the steps in<br>buying your first home</h1>

  <svg class="journey" width="1200" height="784" viewBox="0 0 1200 784" aria-label="Journey map of the home buying steps">
    <!-- markers behind the track -->
    <line class="marker-line" x1="680" y1="224" x2="680" y2="278"/>
    <circle class="marker-dot" cx="680" cy="224" r="3.2"/>
    <text class="marker" x="697" y="227">Idea: get the checklist from</text>
    <text class="marker" x="697" y="241">www.firstkeyloans.com.au</text>

    <line class="marker-line" x1="740" y1="402" x2="810" y2="402"/>
    <circle class="marker-dot" cx="810" cy="402" r="3.2"/>
    <text class="marker" x="825" y="406">Day 1</text>

    <line class="marker-line" x1="755" y1="484" x2="810" y2="484"/>
    <circle class="marker-dot" cx="810" cy="484" r="3.2"/>
    <text class="marker" x="825" y="488">Cooling off period</text>

    <line class="marker-line" x1="326" y1="494" x2="390" y2="494"/>
    <circle class="marker-dot" cx="326" cy="494" r="3.2"/>
    <text class="marker" x="286" y="498">Day 5</text>

    <line class="marker-line" x1="583" y1="536" x2="583" y2="560"/>
    <circle class="marker-dot" cx="583" cy="536" r="3.2"/>
    <text class="marker" x="594" y="539">Day 40</text>

    <line class="marker-line" x1="740" y1="673" x2="810" y2="673"/>
    <circle class="marker-dot" cx="810" cy="673" r="3.2"/>
    <text class="marker" x="823" y="676">Party time!</text>
    <text class="marker" x="823" y="691">Day 42</text>

    <g class="track" fill="none" stroke-width="54" stroke-linecap="butt">
      <!-- row 1 -->
      <path d="M738,303 H649" stroke="#2c90d7"/>
      <path d="M649,303 H556" stroke="#2f94d9"/>
      <path d="M556,303 H460" stroke="#2a8dd4"/>
      <path d="M460,303 H436 A46,46 0 0 0 390,349" stroke="#1f86cf"/>
      <!-- row 2 -->
      <path d="M390,349 A46,46 0 0 0 436,395 H460" stroke="#1e80c8"/>
      <path d="M460,395 H556" stroke="#2687cf"/>
      <path d="M556,395 H649" stroke="#2d8fd6"/>
      <path d="M649,395 H693 A46,46 0 0 1 739,441" stroke="#4ab8ea"/>
      <!-- row 3: cooling off -->
      <path d="M739,441 A46,46 0 0 1 693,487 H649" stroke="#3cb2e8"/>
      <path d="M649,487 H556" stroke="#4ab8ea"/>
      <path d="M556,487 H460" stroke="#41b3e6"/>
      <path d="M460,487 H436 A46,46 0 0 0 390,533" stroke="#48b8ea"/>
      <!-- row 4 -->
      <path d="M390,533 A46,46 0 0 0 436,579 H460" stroke="#1f7ec5"/>
      <path d="M460,579 H556" stroke="#2a8bd2"/>
      <path d="M556,579 H649" stroke="#2185cc"/>
      <path d="M649,579 H693 A46,46 0 0 1 739,625" stroke="#1f82c8"/>
      <!-- row 5 -->
      <path d="M739,625 A46,46 0 0 1 693,671 H649" stroke="var(--cell-teal)"/>
      <path d="M649,671 H556" stroke="#2a8cd4"/>
      <path d="M556,671 H462" stroke="#2b87cf"/>
      <path d="M462,671 H440" stroke="var(--start-red)"/>
    </g>

    <polygon class="start-arrow" fill="var(--start-red)" points="733,303 782,257 782,276 828,276 828,330 782,330 782,350"/>
    <text class="start-label" x="801" y="304">Start</text>

    <g class="cell-numbers">
      <text class="cell-num" x="415" y="304">4</text>
      <text class="cell-num" x="508" y="304">3</text>
      <text class="cell-num" x="603" y="304">2</text>
      <text class="cell-num" x="696" y="304">1</text>
      <text class="cell-num" x="415" y="396">5</text>
      <text class="cell-num" x="508" y="396">6</text>
      <text class="cell-num" x="603" y="396">7</text>
      <text class="cell-num" x="708" y="396">8</text>
      <text class="cell-num" x="415" y="488">12</text>
      <text class="cell-num" x="508" y="488">11</text>
      <text class="cell-num" x="603" y="488">10</text>
      <text class="cell-num" x="708" y="488">9</text>
      <text class="cell-num" x="415" y="580">13</text>
      <text class="cell-num" x="508" y="580">14</text>
      <text class="cell-num" x="603" y="580">15</text>
      <text class="cell-num" x="708" y="580">16</text>
      <text class="cell-num" x="508" y="672">19</text>
      <text class="cell-num" x="603" y="672">18</text>
      <text class="cell-num" x="708" y="672">17</text>
    </g>
  </svg>

  <div class="col-left">
    <div class="step" style="top:182px"><span class="step-num">1.</span><div class="step-body"><p>Start</p></div></div>
    <div class="step" style="top:226px"><span class="step-num">2.</span><div class="step-body"><p>Time to start “Living Like You Have a Mortgage” (It is a good idea a to talk to your Mortgage Broker to help set your savings target and find out how much you can borrow)</p></div></div>
    <div class="step" style="top:276px"><span class="step-num">3.</span><div class="step-body"><p>Get your Pre-Approval in place<br>Make an appointment to talk to your Professional Mortgage Broker to discuss your Lender and interest rate options and get the Pre-Approval under way</p></div></div>
    <div class="step" style="top:331px"><span class="step-num">4.</span><div class="step-body"><p>Appoint your Conveyancer</p><p><span class="sub">a.</span> Make sure you understand the Cost (ask them if this includes reviewing 1 or 2 Contracts in case you miss out on a property)</p><p><span class="sub">b.</span> Ask them – “what do I do once my offer is accepted”</p></div></div>
    <div class="step" style="top:401px"><span class="step-num">5.</span><div class="step-body"><p>Time to go shopping</p></div></div>
    <div class="step" style="top:433px"><span class="step-num">6.</span><div class="step-body"><p>You found the Dream Home - Before you make an offer</p><p><span class="sub">a.</span> Have you done your research? Get a Property Profile report</p><p><span class="sub">b.</span> Ask the agent “what happens if my offer is accepted”</p></div></div>
    <div class="step" style="top:499px"><span class="step-num">7.</span><div class="step-body"><p>Make an offer</p><p><span class="sub">a.</span> Remember this is not binding until you sign the contract and pay the deposit, your ‘just’ making an offer.</p><p><span class="sub">b.</span> Make sure your conveyancer has seen the contract before you sign it</p><p><span class="sub">c.</span> Remember – It is possible to also negotiate a smaller deposit (eg 5%) and longer cooling off period and or a longer Settlement period</p></div></div>
    <div class="step" style="top:599px"><span class="step-num">8.</span><div class="step-body"><p>Offer Accepted</p><p><span class="sub">a.</span> Get the Contract and price to your Broker -make sure they know your Conveyancers Details.</p><p><span class="sub">b.</span> Sign the Contract &amp; pay your deposit (‘Normally’ 0.25% of the purchase price)</p><p><span class="sub">c.</span> Contracts are then “Exchanged” – and Cooling Off starts (normally 5 days)</p></div></div>
    <div class="step" style="top:681px"><span class="step-num">9.</span><div class="step-body"><p>Final Instructions to your Lender/bank</p><p><span class="sub">a.</span> Now that you have the purchase price - You and your Broker need to finalise the loan amount plus the structure (i.e fixed or variable rates)</p><p><span class="sub">b.</span> Your broker will instruct the Lender to proceed</p><p><span class="sub">c.</span> A Valuation is ordered</p></div></div>
  </div>

  <div class="col-right">
    <div class="step" style="top:185px"><span class="step-num">10.</span><div class="step-body"><p>Strata Report / Building Report</p><p><span class="sub">a.</span> If you are buying a Unit – Talk to your conveyancer and get a strata report done.</p><p><span class="sub">b.</span> If you are buying a house – you need a “Pest &amp; Building Report”</p></div></div>
    <div class="step" style="top:245px"><span class="step-num">11.</span><div class="step-body"><p>Formal Approval</p><p><span class="sub">a.</span> When the Valuation is back (3 days) the bank will issue the Formal Approval</p><p><span class="sub">b.</span> Your broker will email you a copy and provide one to your Conveyancer</p></div></div>
    <div class="step" style="top:297px"><span class="step-num">12.</span><div class="step-body"><p>Cooling Off Expires</p><p><span class="sub">a.</span> Now that you have your Approval and your reports are all ok, Cooling can expire and the Contract becomes “Formal”.</p></div></div>
    <div class="step" style="top:345px"><span class="step-num">13.</span><div class="step-body"><p>Lender Prepares Loan Documents.</p><p><span class="sub">a.</span> Work with your broker to make sure they are correct and you understand all the documents before you sign.</p><p><span class="sub">b.</span> Return the signed documents to the Lender.</p></div></div>
    <div class="step" style="top:397px"><span class="step-num">14.</span><div class="step-body"><p>Lender Reviews Documents and is “ready to book settlement”</p></div></div>
    <div class="step" style="top:427px"><span class="step-num">15.</span><div class="step-body"><p>Settlement is Booked</p><p><span class="sub">a.</span> Your Conveyancer will coordinate this with your Lender and the Sellers Conveyancer</p></div></div>
    <div class="step" style="top:465px"><span class="step-num">16.</span><div class="step-body"><p>Cheque Directions</p><p><span class="sub">a.</span> This is where your Conveyancer checks exactly what has been paid, who needs to be paid and where the available money is sitting.</p><p><span class="sub">b.</span> If you have more savings to contribute they will give you the exact number.</p><p><span class="sub">i.</span> please make sure you ask them how to provide the funds. Eg can you transfer it to their Trust Account or do you need a bank cheque?</p></div></div>
    <div class="step" style="top:556px"><span class="step-num">17.</span><div class="step-body"><p>Settlement</p><p><span class="sub">a.</span> Your Conveyancer will contact you</p><p><span class="sub">b.</span> Pick up the keys for the Estate Agent</p><p><span class="sub">c.</span> Pizza party at your place!!!</p></div></div>
    <div class="step" style="top:621px"><span class="step-num">18.</span><div class="step-body"><p>Internet banking and account set up</p><p><span class="sub">a.</span> This may take your Lender 7-10 days after settlement</p><p><span class="sub">b.</span> But you should be proactive and call them to set everything</p></div></div>
    <div class="step" style="top:686px"><span class="step-num">19.</span><div class="step-body"><p>1st payment is Due</p><p><span class="sub">a.</span> Normally 1 month after settlement</p><p><span class="sub">b.</span> The Lender often messes this up - Call them to make sure it is set up how YOU want it</p><p><span class="sub">c.</span> Call them to set up a payment date that suits you - ie the day after your pay</p></div></div>
  </div>

</div>
</body>
</html>
```